Real estate Investment post card Design

I need a post card for Real Estate Marketing.

There are several similar cards on line.
Please see the post cards in this link to clipvora
https://www.clipvora.com/watch?v=pTw8Lm3Qz-Y7
At 1:18 the back of the card is very good.
For front of the card please refer to attached example gif.

Please also check the examples posted by me.

Everything needs to be the same except
1. Teo Gets Homes
2. Phone number 274 859 4167
3. Website www.brookdwellguide.com
4. Email info@brookdwellguide.com
5. Picture needs to be replaced with my picture

The postcards need to be 2 sides and in color

Please let me know

Target Market(s)

Home owners who want to sell their houses for quick settlement and cash

Industry/Entity Type

Real Estate

Requirements
Must have
• I am copying this from another project as i think these instructions are valid for this project as well.
• Attention Designers - Special Requirements
• This project has special US Postcard Design requirements that apply to all submissions. The project is part of a print initiative, meaning that the selected design will be sent directly to print. If you have not, click download the templates below and ensure your design follows them before submitting.
• I plan to print the Post card by printolana in their Jumbo Format... copied below
• Document Trim Size
• 8.52" x 5.47"
• 216 x 139 mm
• 2556 x 1642 pixels
• Full Bleed Size
• Horizontal
• 8.64" x 5.59"
• 219 x 142 mm
• 2592 x 1677 pixels
• NOTE Please make sure you put return address on the post card
• 4837 8TH ST., PO Box. 5926
• NEW HYDE PARK, NY 11040
Nice to have
• Please see if you can add pictures that signify cash $$ and houses in the project. See the attached clipvora.
Should not have
• Too much text on the first page

```html
<!DOCTYPE html>
<html lang="en">
<head>
<meta charset="utf-8">
<title>Teo Gets Homes – Postcard</title>
<link rel="stylesheet" href="https://fonts.googleapis.com/css2?family=Carlito:wght@400;700&family=Jost:wght@400&display=swap">
<style>
  :root {
    --backdrop: #2a2a2a;
    --card: #ffffff;
    --ink: #231f20;
    --gold: #fcc31b;
    --gold-deep: #f0a81c;
    --band: #262626;
    --stamp: #d1d1d1;
    --photo-warm: #d9d2c0;
    --photo-light: #f3f0e8;
    --portrait: #8a8a8a;
  }
  * { box-sizing: border-box; margin: 0; padding: 0; }
  html, body { width: 900px; height: 1200px; overflow: hidden; }
  body {
    position: relative;
    background: var(--backdrop);
    font-family: "Carlito", "Calibri", sans-serif;
    color: var(--ink);
  }
  .card {
    position: absolute;
    left: 79px;
    width: 747px;
    background: var(--card);
    overflow: hidden;
  }
  .card--front { top: 99px; height: 480px; }
  .card--back { top: 623px; height: 482px; }

  /* Front */
  .hero-photo {
    position: absolute;
    left: 0; top: 96px;
    width: 560px; height: 384px;
    background: radial-gradient(ellipse at 40% 55%, var(--photo-warm) 0%, #e6e0d0 45%, var(--photo-light) 75%, rgba(255,255,255,0) 100%);
  }
  .brand-name {
    position: absolute;
    left: 36px; top: 24px;
    font-size: 44px; font-weight: 700;
    letter-spacing: -0.5px;
    color: var(--ink);
  }
  .front-title {
    position: absolute;
    right: 34px; top: 28px;
    font-size: 46px; font-weight: 700;
    line-height: 1;
    white-space: nowrap;
  }
  .front-title .accent { color: var(--gold); }
  .title-rule {
    position: absolute;
    left: 355px; top: 85px;
    width: 358px; height: 4px;
    background: var(--gold);
  }
  .title-rule::before {
    content: "";
    position: absolute; left: 0; top: 0;
    width: 68px; height: 4px;
    background: var(--ink);
  }
  .cash-word {
    position: absolute;
    right: 32px; top: 106px;
    font-size: 72px; font-weight: 700;
    line-height: 1;
    color: var(--gold);
  }
  .cash-word .dollar { color: var(--ink); }
  .promise {
    position: absolute;
    right: 32px; top: 196px;
    text-align: right;
    font-size: 47px; font-weight: 700;
    line-height: 52px;
  }
  .promise .accent { color: var(--gold); }
  .front-blurb {
    position: absolute;
    right: 34px; top: 316px;
    width: 330px;
    text-align: right;
    font-family: "Jost", sans-serif;
    font-size: 10.4px;
    line-height: 13.2px;
  }
  .phone-tag {
    position: absolute;
    right: 0; top: 401px;
    width: 235px; height: 49px;
    background: var(--gold);
    border-radius: 8px 0 0 8px;
    display: flex; align-items: center;
    padding-left: 10px; gap: 8px;
    font-size: 27px;
  }
  .phone-tag svg { width: 26px; height: 26px; }

  /* Back */
  .back-heading {
    position: absolute;
    left: 31px; top: 38px;
    font-size: 32px; font-weight: 700;
    white-space: nowrap;
  }
  .back-heading .accent { color: var(--gold); }
  .back-copy {
    position: absolute;
    left: 32px;
    width: 320px;
    font-family: "Jost", sans-serif;
    font-size: 10.6px;
    line-height: 17.2px;
  }
  .back-copy--one { top: 101px; }
  .back-copy--two { top: 212px; }
  .stamp-box {
    position: absolute;
    left: 615px; top: 30px;
    width: 101px; height: 115px;
    background: var(--stamp);
  }
  .footer-band {
    position: absolute;
    left: 0; bottom: 0;
    width: 100%; height: 49px;
    background: var(--band);
  }
  .agent-tab-wings {
    position: absolute;
    left: 24px; top: 354px;
    width: 337px; height: 79px;
  }
  .agent-tab {
    position: absolute;
    left: 44px; top: 354px;
    width: 295px; height: 128px;
    background: var(--gold);
  }
  .agent-portrait {
    position: absolute;
    left: 8px; top: 4px;
    width: 140px; height: 124px;
    background: linear-gradient(180deg, #b9b9b9 0%, var(--portrait) 60%, #3a3a3a 100%);
  }
  .agent-name {
    position: absolute;
    right: 6px; top: 20px;
    font-size: 25px; font-weight: 700;
    color: #ffffff;
    white-space: nowrap;
  }
  .agent-phone {
    position: absolute;
    right: 6px; top: 54px;
    font-size: 24px;
    white-space: nowrap;
  }
  .agent-links {
    position: absolute;
    right: 4px; top: 84px;
    text-align: right;
    font-family: "Jost", sans-serif;
    font-size: 11px;
    line-height: 13px;
  }
</style>
</head>
<body>

<section class="card card--front">
  <div class="hero-photo" role="img" aria-label="Model house resting on stacks of hundred-dollar bills"></div>
  <div class="brand-name">Hearthly</div>
  <h1 class="front-title"><span class="accent">Teo</span> Gets Homes</h1>
  <div class="title-rule"></div>
  <div class="cash-word">CA<span class="dollar">$</span>H</div>
  <div class="promise">
    <span class="accent">Any</span> Condition<br>
    Any <span class="accent">Situation</span>
  </div>
  <p class="front-blurb">Lorem ipsum dolor sit amet, consectetur adipiscing elit. Nam id enim ac erat blandit tristique ac a augue. Cum sociis natoque penatibus et magnis dis parturient montes, nascetur ridiculus mus. Fusce congue, metus nec eleifend euismod, erat elit luctus dolor, pellentesque dapibus leo velit id nunc</p>
  <div class="phone-tag">
    <svg viewBox="0 0 24 24" aria-hidden="true">
      <path fill="#231f20" d="M6.6 10.8c1.4 2.8 3.8 5.1 6.6 6.6l2.2-2.2c.3-.3.7-.4 1-.2 1.1.4 2.3.6 3.6.6.6 0 1 .4 1 1V20c0 .6-.4 1-1 1C10.6 21 3 13.4 3 4c0-.6.4-1 1-1h3.5c.6 0 1 .4 1 1 0 1.3.2 2.5.6 3.6.1.3 0 .7-.2 1L6.6 10.8z"/>
      <path fill="none" stroke="#231f20" stroke-width="1.6" stroke-linecap="round" d="M14 3.5a7 7 0 0 1 6.5 6.5M14 7a3.6 3.6 0 0 1 3 3"/>
    </svg>
    <span>274 859 4167</span>
  </div>
</section>

<section class="card card--back">
  <h2 class="back-heading">Lorem ipsum <span class="accent">dolor sit amet</span></h2>
  <p class="back-copy back-copy--one">Lorem ipsum dolor sit amet, consectetur adipiscing elit. Nam id enim ac erat blandit tristique ac a augue. Cum sociis natoque penatibus et magnis dis parturient montes, nascetur ridiculus mus. Fusce congue, metus nec eleifend euismod, erat elit luctus dolor, pellentesque dapibus leo velit id nunc</p>
  <p class="back-copy back-copy--two">Integer accumsan eget risus non fringilla. Sed venenatis, orci a interdum egestas, leo tellus fringilla sem, vitae condimentum purus quam a nisl. Morbi congue rutrum scelerisque. Nunc vel pretium purus. Fusce non fermentum libero. Pellentesque bibendum felis in ex luctus malesuada eu vulputate est. In eget consequat dolor.</p>
  <div class="stamp-box"></div>
  <div class="footer-band"></div>
  <svg class="agent-tab-wings" viewBox="0 0 337 79" aria-hidden="true">
    <polygon points="10,0 327,0 337,79 0,79" fill="var(--gold-deep)"/>
  </svg>
  <div class="agent-tab">
    <div class="agent-portrait" role="img" aria-label="Portrait photo of the agent in suit and tie"></div>
    <div class="agent-name">Teo Gets Homes</div>
    <div class="agent-phone">274 859 4167</div>
    <div class="agent-links">www.brookdwellguide.com<br>info@brookdwellguide.com</div>
  </div>
</section>

</body>
</html>
```